Delcourt Realty Business Cards

Design business card

Target Market(s)

High-End Buyer of Real Estate over $1 million dollars

Industry/Entity Type

Realtor

Contact Information for Business Card

Lena Delcourt R(S) LIC.# 41972
Cell 555 246-1938
Email Lena@Delcourt.example
Website IsleFreshHomes.example

Also Need Cards for:

Hank Delcourt R(B) LIC# 69418
C 555 613-7052
E Hank@Delcourt.example
W IsleFreshHomes.example

Colors

Designer to choose colors to be used in the design.

Requirements
Must have
• Address on back:
• 287 Pohaku Cir. , Hale Nui HI 96700
• Logo on back
Nice to have
• I would like the phone numbers and email address to be big so people can read it easily
Should not have
• Very small print Except For: address (287 Pohaku Cir. Wailea HI 96753)

```html
<!DOCTYPE html>
<html lang="en">
<head>
<meta charset="utf-8">
<title>Delcourt Realty Business Cards</title>
<link rel="stylesheet" href="https://fonts.googleapis.com/css2?family=Source+Sans+3:wght@400;700&display=swap">
<style>
  :root {
    --board-light: #4b4b4b;
    --board-dark: #121212;
    --brand-blue: #2e3192;
    --ink: #1a1a1a;
    --paper: #ffffff;
  }
  * { margin: 0; padding: 0; box-sizing: border-box; }
  html, body { width: 1200px; height: 1200px; overflow: hidden; }
  body {
    position: relative;
    font-family: "Source Sans 3", sans-serif;
    background: radial-gradient(circle at 30% 50%, var(--board-light) 0%, #2a2a2a 45%, var(--board-dark) 100%);
  }

  .brand-showcase {
    position: absolute;
    left: 99px; top: 332px;
    width: 326px; height: 537px;
    display: flex; flex-direction: column;
    align-items: center; justify-content: center;
    color: var(--paper);
    font-weight: 700;
    font-size: 58px;
    line-height: 1.15;
    letter-spacing: 3px;
    text-transform: uppercase;
    text-align: center;
  }

  .card {
    position: absolute;
    background: var(--paper);
    box-shadow: 0 4px 14px rgba(0,0,0,0.45);
    overflow: hidden;
  }
  .card--front-lena { left: 622px; top: 116px; width: 490px; height: 272px; }
  .card--front-hank { left: 618px; top: 470px; width: 496px; height: 275px; }
  .card--back { left: 622px; top: 826px; width: 493px; height: 277px; background: var(--brand-blue); }

  .card__panel { position: absolute; inset: 0; width: 100%; height: 100%; }
  .card__panel polygon { fill: var(--brand-blue); }

  .agent { position: absolute; left: 26px; top: 14px; color: var(--ink); }
  .agent__name { font-weight: 700; font-size: 23px; line-height: 1.2; }
  .agent__licence { font-size: 14.5px; line-height: 1.3; }

  .contact-list { list-style: none; }
  .contact-item {
    position: absolute;
    left: 36px;
    height: 28px;
    display: flex; align-items: center;
  }
  .contact-item__icon { width: 28px; height: 28px; flex: none; }
  .contact-item__text {
    position: absolute; left: 68px;
    color: var(--paper);
    font-weight: 700; font-size: 19.5px;
    white-space: nowrap;
  }

  .card-brand {
    position: absolute;
    left: 346px; top: 56px;
    width: 110px; height: 160px;
    display: flex; flex-direction: column;
    align-items: center; justify-content: center;
    color: var(--paper);
    font-weight: 700; font-size: 17px;
    letter-spacing: 2px;
    line-height: 1.4;
    text-transform: uppercase;
    text-align: center;
  }

  .back-brand {
    position: absolute;
    left: 70px; top: 50px;
    width: 354px; height: 117px;
    display: flex; flex-direction: column;
    align-items: center; justify-content: center;
    color: var(--paper);
    font-weight: 700; font-size: 40px;
    line-height: 1.15;
    letter-spacing: 4px;
    text-transform: uppercase;
    text-align: center;
  }
  .address {
    position: absolute;
    left: 98px; top: 196px;
    display: flex; align-items: center; gap: 12px;
    color: var(--paper);
    font-weight: 700; font-size: 17px;
    white-space: nowrap;
  }
  .address__icon { width: 28px; height: 28px; flex: none; }
</style>
</head>
<body>

<div class="brand-showcase"><span>Delcourt</span><span>Realty</span></div>

<section class="card card--front-lena">
  <svg class="card__panel" viewBox="0 0 612 340" preserveAspectRatio="none" aria-hidden="true">
    <polygon points="555,0 612,0 612,340 100,340 106,119"/>
  </svg>
  <div class="agent">
    <div class="agent__name">Lena Delcourt</div>
    <div class="agent__licence">R(S) LIC.# 41972</div>
  </div>
  <ul class="contact-list">
    <li class="contact-item" style="top:118px">
      <svg class="contact-item__icon" viewBox="0 0 28 28" aria-hidden="true"><circle cx="14" cy="14" r="14" fill="#000"/><path d="M9 7.5c1-.6 1.8-.4 2.3.4l1.2 2c.4.7.2 1.4-.4 1.9l-.8.6c.7 1.6 2 3 3.6 3.8l.6-.8c.5-.6 1.2-.8 1.9-.4l2 1.2c.8.5 1 1.3.4 2.3-.8 1.3-2.2 1.9-3.6 1.4-3.8-1.4-6.6-4.2-8-8-.5-1.4.1-2.8 1.4-3.6z" fill="#fff"/></svg>
      <span class="contact-item__text">555 246-1938</span>
    </li>
    <li class="contact-item" style="top:170px">
      <svg class="contact-item__icon" viewBox="0 0 28 28" aria-hidden="true"><circle cx="14" cy="14" r="14" fill="#000"/><rect x="7.5" y="9.5" width="13" height="9" fill="none" stroke="#fff" stroke-width="1.5"/><path d="M7.5 9.5l6.5 5 6.5-5M7.5 18.5l4.5-4.5M20.5 18.5l-4.5-4.5" fill="none" stroke="#fff" stroke-width="1.3"/></svg>
      <span class="contact-item__text">Lena@Delcourt.example</span>
    </li>
    <li class="contact-item" style="top:220px">
      <svg class="contact-item__icon" viewBox="0 0 28 28" aria-hidden="true"><circle cx="14" cy="14" r="14" fill="#000"/><g fill="none" stroke="#fff" stroke-width="1.4"><circle cx="14" cy="14" r="7"/><ellipse cx="14" cy="14" rx="3" ry="7"/><path d="M7 14h14M8 10.5h12M8 17.5h12"/></g></svg>
      <span class="contact-item__text">IsleFreshHomes.example</span>
    </li>
  </ul>
  <div class="card-brand"><span>Delcourt</span><span>Realty</span></div>
</section>

<section class="card card--front-hank">
  <svg class="card__panel" viewBox="0 0 619 343" preserveAspectRatio="none" aria-hidden="true">
    <polygon points="560,0 619,0 619,343 101,343 107,119"/>
  </svg>
  <div class="agent">
    <div class="agent__name">Hank Delcourt</div>
    <div class="agent__licence">R(B) LIC# 69418</div>
  </div>
  <ul class="contact-list">
    <li class="contact-item" style="top:120px">
      <svg class="contact-item__icon" viewBox="0 0 28 28" aria-hidden="true"><circle cx="14" cy="14" r="14" fill="#000"/><path d="M9 7.5c1-.6 1.8-.4 2.3.4l1.2 2c.4.7.2 1.4-.4 1.9l-.8.6c.7 1.6 2 3 3.6 3.8l.6-.8c.5-.6 1.2-.8 1.9-.4l2 1.2c.8.5 1 1.3.4 2.3-.8 1.3-2.2 1.9-3.6 1.4-3.8-1.4-6.6-4.2-8-8-.5-1.4.1-2.8 1.4-3.6z" fill="#fff"/></svg>
      <span class="contact-item__text">555 613-7052</span>
    </li>
    <li class="contact-item" style="top:172px">
      <svg class="contact-item__icon" viewBox="0 0 28 28" aria-hidden="true"><circle cx="14" cy="14" r="14" fill="#000"/><rect x="7.5" y="9.5" width="13" height="9" fill="none" stroke="#fff" stroke-width="1.5"/><path d="M7.5 9.5l6.5 5 6.5-5M7.5 18.5l4.5-4.5M20.5 18.5l-4.5-4.5" fill="none" stroke="#fff" stroke-width="1.3"/></svg>
      <span class="contact-item__text">Hank@Delcourt.example</span>
    </li>
    <li class="contact-item" style="top:222px">
      <svg class="contact-item__icon" viewBox="0 0 28 28" aria-hidden="true"><circle cx="14" cy="14" r="14" fill="#000"/><g fill="none" stroke="#fff" stroke-width="1.4"><circle cx="14" cy="14" r="7"/><ellipse cx="14" cy="14" rx="3" ry="7"/><path d="M7 14h14M8 10.5h12M8 17.5h12"/></g></svg>
      <span class="contact-item__text">IsleFreshHomes.example</span>
    </li>
  </ul>
  <div class="card-brand" style="left:352px"><span>Delcourt</span><span>Realty</span></div>
</section>

<section class="card card--back">
  <div class="back-brand"><span>Delcourt</span><span>Realty</span></div>
  <div class="address">
    <svg class="address__icon" viewBox="0 0 28 28" aria-hidden="true"><circle cx="14" cy="14" r="14" fill="#000"/><path d="M14 6.5a5 5 0 0 0-5 5c0 3.6 5 9.5 5 9.5s5-5.9 5-9.5a5 5 0 0 0-5-5z" fill="#fff"/><circle cx="14" cy="11.5" r="1.8" fill="#000"/></svg>
    <span>287 Pohaku Cir. , Hale Nui HI 96700</span>
  </div>
</section>

</body>
</html>
```